bramblecrest paving card makeover

were a excavation/paving contractor from Monterey ca, I'm looking to have a card designed front and back that has company details on the front and a list of the services we offer on the back.

Target Market(s)

home owners property management companies

Industry/Entity Type

Contractor

Contact Information for Business Card

bramblecrest paving 418 larkmoor st Monterey ca. licensed, insured and bonded
lic#657920 gerald pinsky operations manager

Font styles to use
Serif
Sans Serif

Colors
f78f20

Requirements
Must have
• a list of my services on back, asphalt construction and maintenance, drainage, foundations, retaining walls, chip seals, excavation, grading, landscape ground work, interlocking paver, hydro-seeding, structured and driveway demolition, utility trenching and stump removal.
Nice to have
• my new domain and page address I'm acquiring from pixel bazaar.

```html
<!DOCTYPE html>
<html lang="en">
<head>
<meta charset="utf-8">
<title>Bramblecrest Paving – Services</title>
<link href="https://fonts.googleapis.com/css2?family=Montserrat:wght@600;700&display=swap" rel="stylesheet">
<style>
  :root {
    --card-bg: #231f20;
    --brand-orange: #f78f20;
  }
  * { margin: 0; padding: 0; box-sizing: border-box; }
  html, body {
    width: 1200px;
    height: 686px;
    overflow: hidden;
    background: var(--card-bg);
  }
  .card-back {
    position: relative;
    width: 1200px;
    height: 686px;
    background: var(--card-bg);
    color: var(--brand-orange);
    font-family: "Montserrat", Arial, sans-serif;
  }
  .services-title {
    position: absolute;
    left: 49px;
    top: 40px;
    font-size: 50px;
    font-weight: 600;
    line-height: 1.1;
  }
  .service-list {
    position: absolute;
    top: 124px;
    list-style: none;
    font-size: 32px;
    font-weight: 600;
    line-height: 36px;
  }
  .service-list--left { left: 110px; }
  .service-list--right { left: 560px; }
  .service-list li {
    position: relative;
    margin-bottom: 4.8px;
    white-space: nowrap;
  }
  .service-list li::before {
    content: "";
    position: absolute;
    left: -18px;
    top: 16px;
    width: 5px;
    height: 5px;
    border-radius: 50%;
    background: var(--brand-orange);
  }
  .brand-name {
    position: absolute;
    left: 0;
    right: 0;
    top: 556px;
    text-align: center;
    font-size: 44px;
    font-weight: 700;
    letter-spacing: 1px;
    line-height: 1;
  }
</style>
</head>
<body>
  <div class="card-back">
    <h1 class="services-title">Services:</h1>

    <ul class="service-list service-list--left">
      <li>Asphalt construction<br>and maintenance</li>
      <li>Drainage</li>
      <li>Foundations</li>
      <li>Retaining walls</li>
      <li>Chip seals</li>
      <li>Excavation</li>
      <li>Grading</li>
      <li>Landscape ground work</li>
    </ul>

    <ul class="service-list service-list--right">
      <li>Landscape ground work</li>
      <li>Interlocking Paver</li>
      <li>Hydro-seeding</li>
      <li>Structure and driveway demolition</li>
      <li>Utility trenching</li>
      <li>Stump removal</li>
    </ul>

    <div class="brand-name">BRAMBLECREST PAVING</div>
  </div>
</body>
</html>
```